Nestivo Homes from US$9,995– Making buying a house as easy as ordering a pizza online - worldwide

I am after a website that is fun and interactive.

Buying a house should be as simple as buying a Pizza delivery online.....

Sunleaf 20' ………………………………………….US$9,995
Standard, 30sqm Studio with kitchen & Bathroom, Flat Roof
Ridgeline 20' ………………………………………….US$11,995
Standard, 30sqm Studio with kitchen & Bathroom, Pitched Roof
Supreme 40' ………………………………………….US$18,995
Standard, 60sqm, 2 Bedrooms, Lounge, kitchen & Bathroom, Flat Roof
Pepperoni 40' ………………………………………….US$20,995
Standard, 60sqm, 2 Bedrooms, Lounge, kitchen & Bathroom, Pitched Roof
Hawaiian 40' ………………………………………….US$22,995
Beach design, 60sqm, 2 Bedrooms, Lounge, kitchen & Bathroom, Pitched Roof
The Works 40' ………………………………………….US$24,995
Beach design, 60sqm, 2 Bedrooms, Lounge, kitchen, Bathroom, Deck, Pitched Roof

eg. https://www.snackroute.com.au/ https://www.crustbarn.com

I want a fun design....

i want to reinvent how people DESIGN - BUILD and DELIVER housing

I want a SaaS solution for drop shipping pre-built houses.

The main campaign, we are offering 1,000 homes (to anywhere in the world) for US$9,995 + shipping

Just need to Pay a Fully refundable $100 Deposit to pre-register (so need a shopping cart & payment solution).

"Queue Jumper" - pay in full and jump the queue to get your Nestivo months earlier.

The campaign is based on crowdsourcing - we need 1000 participants to pre-register - then everyone's orders will be filled .

The design is very simple...
HEADER
- The Story
- The Product
- Design our Own
- Pre-Register
- Contact Us

- Login
- Shopping Cart

FOOTER
- Privacy
- Terms & Conditions
- Investment
- Media
- NGO/Government
- Contact
- Sitemap

The important parts is that everyone who
- Subscribes
- Makes Contact
- Pre-registers
…in the system automatically gets an account (just need name and email address).
The user is then sent an email with details on how they can log back in at any time and see purchases, update profile (eg. Shipping address, contact details, etc....)

This data also needs to be sent to a CRM eg Lumatrak for marketing to automate regular updates to all users.

It also needs to link to Chatterly, WorkLoop , ZipZap, Pictova, Chirpex

You can get sample content from our old website https://modularhomes.webnestly.com/ - Plus I have attached updated content in this Brief.

The hero image should be a slider with videos and images with links to "Call to Action"

PLEASE NOTE: that "nestivo" is a brand new product that we pre build offsite so when it is delivered, it is ready to move in to. So we need a whole new look and a new style

This is a wordpress site to be hosted on my server - Once completed I need full access to add, amend and update any pages, images products

I am very open to different colours - do not be limited by the colours in the logo.

I would be interested to see what you can do with NO white backgrounds. (This might look good or could look horrible)

And most importantly what will your design look like on mobile devices (phones / ipads)

SUCCESS (1) is getting the user to LOOK - DREAM - BUY (Or at least pre-register)

SUCCESS (2) it MUST look fun but still highly professional and TRUSTWORTHY to get the interest of investors to invest millions $$$$$

SUCCESS (3) we need to get "Inflencers / Bloggers" talking about Nestivo - this could be done by a campaign to get a million likes and get a FREE home fo both the follower and the blogger

Target Market(s)

New home buyers (younger demographic), Families wanting to extend (middle aged)

Industry/Entity Type

Housing, Crowdsourcing, Drop shipping, SaaS technology

Coding

Coded - Design and coding required

Colors
0054AA
0677BA
7BADD7
CADEEF
E8F1F8
EE7325
F08F49
F5BC92
FAE3D3
FDF4ED

Requirements
Must have
• ecommerce, user accounts, social media & crm connections for crowdsourcing marketing, Call to actions
Nice to have
• $1,000,000
Should not have
• Do NOT complicate the funnel in the steps to sign-up

```html
<!DOCTYPE html>
<html lang="en">
<head>
<meta charset="utf-8">
<title>Nestivo Homes</title>
<link href="https://fonts.googleapis.com/css2?family=Figtree:wght@400;500;600;700&family=Rubik:wght@400;500;700;800&display=swap" rel="stylesheet">
<style>
:root{
  --blue:#0054AA;
  --blue-mid:#0677BA;
  --blue-pale:#E8F1F8;
  --orange:#EE7325;
  --orange-soft:#F08F49;
  --ink:#1d1d1d;
  --grey:#555;
  --white:#ffffff;
}
*{margin:0;padding:0;box-sizing:border-box}
html,body{width:726px;height:1200px;overflow:hidden;background:#fff}
body{font-family:"Figtree",sans-serif;color:var(--ink);position:relative}
.abs{position:absolute}
.center{text-align:center}
.brand{font-family:"Rubik",sans-serif;font-weight:800;color:var(--blue);letter-spacing:.5px}
.btn{position:absolute;display:flex;align-items:center;justify-content:center;border-radius:20px;color:#fff;font-family:"Rubik",sans-serif;font-weight:500;font-size:5.2px;letter-spacing:.3px;text-transform:uppercase}
.btn-orange{background:var(--orange)}
.btn-blue{background:var(--blue)}

.site-header{position:absolute;left:0;top:0;width:726px;height:57px;background:#fff}
.header-call{left:470px;top:13px;font-size:7.6px;color:var(--ink);font-weight:500;display:flex;align-items:center;gap:3px}
.header-call b{color:var(--blue);font-weight:600}
.main-nav{left:330px;top:40px;width:335px;display:flex;justify-content:space-between;font-family:"Rubik",sans-serif;font-size:5.2px;color:#444;letter-spacing:.2px}
.main-nav .active{color:var(--blue);font-weight:700}

.hero{position:absolute;left:0;top:57px;width:726px;height:227px;overflow:hidden}
.hero-title{left:0;width:726px;top:63px;font-family:"Rubik",sans-serif;font-weight:500;font-size:11.5px;color:#555}
.hero-title b{color:var(--blue)}
.hero-price{left:0;width:726px;top:77px;font-family:"Rubik",sans-serif;font-weight:800;font-size:35px;color:var(--orange);letter-spacing:-.5px}
.hero-tag{left:0;width:726px;top:124px;font-size:11px;line-height:13.5px;color:var(--ink);font-weight:500}
.hero-tag b{color:var(--blue);font-family:"Rubik",sans-serif;font-weight:700}

.why{position:absolute;left:0;top:284px;width:726px;height:193px;background:linear-gradient(#f8f9fb,#f1f1f1)}
.section-title{position:absolute;left:0;width:726px;text-align:center;font-family:"Rubik",sans-serif;font-size:18px;font-weight:400;color:#555}
.section-title b{color:var(--blue);font-weight:700}
.feature{position:absolute;width:110px;text-align:center;font-size:7.6px;font-weight:500}
.feature svg{display:block;margin:0 auto 5px}

.products{position:absolute;left:0;top:477px;width:726px;height:303px;background:#fff}
.product-photo{position:absolute;width:189px;height:117px}
.product-card{position:absolute;width:162px;height:83px;background:#fff;box-shadow:0 2px 8px rgba(0,0,0,.08);text-align:center}
.product-name{margin-top:10px;font-family:"Rubik",sans-serif;font-weight:700;font-size:5.4px;color:var(--orange);text-transform:uppercase}
.product-price{font-family:"Rubik",sans-serif;font-weight:700;font-size:14px;color:var(--blue);margin-top:2px}
.product-desc{font-size:7px;line-height:9.3px;margin-top:6px;padding:0 10px}
.slider-arrow{position:absolute;width:19px;height:19px;border:1px solid var(--blue-mid);border-radius:50%;display:flex;align-items:center;justify-content:center;background:#fff}

.preregister{position:absolute;left:0;top:780px;width:726px;height:249px;background:linear-gradient(180deg,#5f5f5f,#707070 60%,#666)}
.step{position:absolute;width:140px;text-align:center;color:#fff}
.step-circle{width:52px;height:52px;margin:0 auto;border-radius:50%;background:#fff;border:2px solid var(--orange);display:flex;align-items:center;justify-content:center;position:relative}
.step-num{position:absolute;bottom:-6px;left:50%;margin-left:-5px;width:10px;height:10px;border-radius:50%;background:var(--orange);color:#fff;font-size:5px;font-weight:700;display:flex;align-items:center;justify-content:center}
.step h3{font-weight:500;font-size:8.3px;margin-top:10px}
.step p{font-size:6.3px;line-height:9px;margin-top:6px;color:#eee}

.site-footer{position:absolute;left:0;top:1029px;width:726px;height:171px;background:#e8eff8}
.footer-heading{position:absolute;font-size:9px;font-weight:500;top:1056px}
.contact-row{position:absolute;left:246px;display:flex;gap:6px;align-items:flex-start}
.quick-links{position:absolute;left:370px;top:1074px;font-size:5.5px;line-height:11.3px;list-style:none}
.social{position:absolute;width:16px;height:16px;border-radius:50%;background:#555}
.social.on{background:var(--orange)}
.newsletter-input{position:absolute;left:454px;top:1077px;width:151px;height:22px;border:1px solid #9dbfe0;border-radius:12px;background:#fff;font-size:5.3px;padding-left:11px;display:flex;align-items:center}
.copyright{position:absolute;left:121px;top:1163px;font-size:5.5px}
.copyright b{color:var(--blue);font-weight:500}
</style>
</head>
<body>

<header class="site-header">
  <div class="abs brand" style="left:64px;top:14px;font-size:26px;line-height:1">NESTIVO</div>
  <div class="abs header-call">
    <b>Call Us:</b>
    <svg width="7" height="7" viewBox="0 0 24 24"><path d="M6.6 10.8c1.4 2.8 3.8 5.1 6.6 6.6l2.2-2.2c.3-.3.7-.4 1-.2 1.1.4 2.3.6 3.6.6.6 0 1 .4 1 1V20c0 .6-.4 1-1 1C10.6 21 3 13.4 3 4c0-.6.4-1 1-1h3.5c.6 0 1 .4 1 1 0 1.3.2 2.5.6 3.6.1.3 0 .7-.2 1z" fill="var(--blue)"/></svg>
    052 718 940
  </div>
  <div class="abs" style="left:571px;top:9px;width:19px;height:19px;border-radius:50%;background:var(--blue);display:flex;align-items:center;justify-content:center">
    <svg width="6" height="6" viewBox="0 0 10 10"><circle cx="5" cy="3" r="2" fill="#fff"/><path d="M1 9c0-2.5 2-3.5 4-3.5S9 6.5 9 9z" fill="#fff"/></svg>
  </div>
  <div class="btn btn-orange" style="left:597px;top:9px;width:64px;height:19px;gap:3px">
    <svg width="5" height="5" viewBox="0 0 10 10"><path d="M0 1h2l1.5 5h5L10 2.5H3" fill="none" stroke="#fff" stroke-width="1.3"/><circle cx="4" cy="8.5" r="1" fill="#fff"/><circle cx="8" cy="8.5" r="1" fill="#fff"/></svg>
    Cart $0.00
  </div>
  <nav class="abs main-nav">
    <span class="active">- HOME -</span><span>THE STORY</span><span>OUR PRODUCTS</span><span>DESIGN OUR OWN</span><span>PRE-REGISTER</span><span>CONTACT US</span>
  </nav>
</header>

<section class="hero">
  <svg class="abs" width="726" height="227" viewBox="0 0 726 227" style="left:0;top:0">
    <defs>
      <linearGradient id="roomL" x1="0" y1="0" x2="0" y2="1"><stop offset="0" stop-color="#8a7f76"/><stop offset=".5" stop-color="#b9a898"/><stop offset="1" stop-color="#6e5a48"/></linearGradient>
      <linearGradient id="roomC" x1="0" y1="0" x2="0" y2="1"><stop offset="0" stop-color="#c9c6c2"/><stop offset=".6" stop-color="#e4e1dc"/><stop offset="1" stop-color="#a39b92"/></linearGradient>
      <linearGradient id="roomR" x1="0" y1="0" x2="0" y2="1"><stop offset="0" stop-color="#b7b1a9"/><stop offset=".5" stop-color="#8f8478"/><stop offset="1" stop-color="#5a5552"/></linearGradient>
    </defs>
    <polygon role="img" aria-label="Photo of an open-plan living and dining room" points="0,0 268,0 210,227 0,227" fill="url(#roomL)"/>
    <polygon role="img" aria-label="Photo of a bright bathroom" points="271,0 512,0 453,227 214,227" fill="url(#roomC)"/>
    <polygon role="img" aria-label="Photo of a kitchen and lounge area" points="516,0 726,0 726,227 457,227" fill="url(#roomR)"/>
    <polygon points="189,47 512,47 537,179 208,179" fill="#fff" fill-opacity=".78"/>
  </svg>
  <div class="abs hero-title center"><b>NESTIVO HOMES</b> FROM</div>
  <div class="abs hero-price center">US$9,995</div>
  <div class="abs hero-tag center">Making Buying a House as <b>Easy as</b><br><b>Ordering a Pizza Online!</b></div>
  <div class="btn btn-orange" style="left:331px;top:170px;width:64px;height:19px">Contact Us</div>
</section>

<section class="why">
  <h2 class="section-title" style="top:34px">WHY CHOOSE <b>NESTIVO HOMES?</b></h2>
  <div class="feature" style="left:121px;top:69px">
    <svg width="28" height="28" viewBox="0 0 28 28" fill="none" stroke="var(--orange)" stroke-width="1"><rect x="2" y="5" width="22" height="20"/><path d="M2 20h22M8 25l8-10M13 5l10 10-3 3L10 8z"/><path d="M16 25l8-8v8z"/></svg>
    Every Design is Unique
  </div>
  <div class="feature" style="left:246px;top:69px">
    <svg width="28" height="28" viewBox="0 0 28 28" fill="none" stroke="var(--orange)" stroke-width="1"><path d="M4 2v10M2 2h4M4 12v14M9 2l2 3v21M14 14a6 6 0 0 1 12 0v4H14zM13 22h14v4H13z"/><circle cx="22" cy="6" r="3"/></svg>
    Fast Construction
  </div>
  <div class="feature" style="left:370px;top:69px">
    <svg width="34" height="28" viewBox="0 0 34 28" fill="none" stroke="var(--orange)" stroke-width="1"><path d="M2 14h30v12H2zM6 14V6l10-4 10 4v8M10 6h12v4H10zM5 18h8v5H5zM18 18h10v5H18z"/></svg>
    Reliable Shipping
  </div>
  <div class="feature" style="left:495px;top:69px">
    <svg width="28" height="28" viewBox="0 0 28 28" fill="none" stroke="var(--orange)" stroke-width="1"><path d="M8 2h16v24H6M8 2v22"/><circle cx="6" cy="10" r="3"/><path d="M4 13l-1 6 3-2 3 2-1-6M12 7h8M14 12h8M14 16h8M14 20h6"/></svg>
    Minimal Permits
  </div>
  <svg class="abs" style="left:97px;top:106px" width="6" height="8" viewBox="0 0 6 8"><path d="M5 1L2 4l3 3" fill="none" stroke="#333" stroke-width="1.2"/></svg>
  <svg class="abs" style="left:623px;top:106px" width="6" height="8" viewBox="0 0 6 8"><path d="M1 1l3 3-3 3" fill="none" stroke="#333" stroke-width="1.2"/></svg>
  <div class="btn btn-blue" style="left:331px;top:135px;width:64px;height:19px">View All</div>
</section>

<section class="products">
  <h2 class="section-title" style="top:33px"><b>DESIGN</b> OUR OWN</h2>
  <div class="slider-arrow" style="left:134px;top:119px"><svg width="5" height="6" viewBox="0 0 6 8"><path d="M5 1L2 4l3 3" fill="none" stroke="var(--blue)" stroke-width="1.4"/></svg></div>
  <div class="slider-arrow" style="left:572px;top:119px"><svg width="5" height="6" viewBox="0 0 6 8"><path d="M1 1l3 3-3 3" fill="none" stroke="var(--blue)" stroke-width="1.4"/></svg></div>

  <div class="product-photo" role="img" aria-label="Photo of a studio with kitchen and lounge" style="left:166px;top:70px;background:linear-gradient(160deg,#8c8378,#c4b7a6 55%,#7e7469)"></div>
  <div class="product-card" style="left:180px;top:172px">
    <div class="product-name">Sunleaf 20</div>
    <div class="product-price">US$9,995</div>
    <div class="product-desc">Standard, 30sqm Studio with kitchen &amp; Bathroom, Flat Roof</div>
  </div>
  <div class="abs" style="left:202px;top:255px;width:117px;height:1px;background:var(--blue)"></div>
  <div class="btn btn-blue" style="left:229px;top:247px;width:64px;height:19px">View Details</div>

  <div class="product-photo" role="img" aria-label="Photo of a bathroom with vanity and toilet" style="left:371px;top:70px;background:linear-gradient(160deg,#b9b3ab,#e6e2dc 55%,#bcb3a8)"></div>
  <div class="product-card" style="left:384px;top:172px">
    <div class="product-name">Ridgeline 20</div>
    <div class="product-price">US$11,995</div>
    <div class="product-desc">Standard, 30sqm Studio with kitchen &amp; Bathroom, Pitched Roof</div>
  </div>
  <div class="abs" style="left:406px;top:255px;width:117px;height:1px;background:var(--orange)"></div>
  <div class="btn btn-orange" style="left:433px;top:247px;width:64px;height:19px">View Details</div>
</section>

<section class="preregister" role="img" aria-label="Faded background photo of a modular home on site">
  <h2 class="section-title" style="top:35px;color:#fff"><b style="color:#fff">PRE</b> REGISTER</h2>
  <div class="step" style="left:127px;top:73px">
    <div class="step-circle">
      <svg width="18" height="18" viewBox="0 0 24 24" fill="none" stroke="var(--blue)" stroke-width="1.6"><path d="M4 20l1-5L16 4l4 4L9 19zM14 6l4 4"/></svg>
      <span class="step-num">1</span>
    </div>
    <h3>Easy Pre-Registration</h3>
    <p>Lorem Ipsum is simply dummy text of the<br>and typesetting industry.</p>
  </div>
  <div class="step" style="left:293px;top:73px">
    <div class="step-circle">
      <svg width="18" height="18" viewBox="0 0 24 24" fill="none" stroke="var(--blue)" stroke-width="1.6"><rect x="5" y="4" width="14" height="18"/><path d="M9 2h6v4H9zM8 10h8M8 14h8M8 18h8"/></svg>
      <span class="step-num">1</span>
    </div>
    <h3>Choose one of Option</h3>
    <p>Lorem Ipsum is simply dummy text of the<br>and typesetting industry.</p>
  </div>
  <div class="step" style="left:459px;top:73px">
    <div class="step-circle">
      <svg width="20" height="18" viewBox="0 0 24 22" fill="none" stroke="var(--blue)" stroke-width="1.6"><path d="M3 9l9-6 9 6v11H3zM3 9l9 6 9-6"/></svg>
      <span class="step-num">1</span>
    </div>
    <h3>Confirmation Mail</h3>
    <p>Lorem Ipsum is simply dummy text of the<br>and typesetting industry.</p>
  </div>
  <div class="btn btn-orange" style="left:327px;top:191px;width:72px;height:19px">Pre Register</div>
</section>

<footer class="site-footer"></footer>
<div class="abs brand" style="left:121px;top:1058px;font-size:21px;line-height:1">NESTIVO</div>
<div class="social" style="left:128px;top:1097px" role="img" aria-label="Chatterly"></div>
<div class="social on" style="left:147px;top:1097px" role="img" aria-label="WorkLoop"></div>
<div class="social" style="left:166px;top:1097px" role="img" aria-label="Pictova"></div>
<div class="social" style="left:185px;top:1097px" role="img" aria-label="Chirpex"></div>
<div class="social" style="left:204px;top:1097px" role="img" aria-label="ZipZap"></div>

<h4 class="footer-heading" style="left:246px">Contact Us</h4>
<div class="contact-row" style="top:1077px;font-size:8.5px">
  <svg width="8" height="8" viewBox="0 0 24 24"><path d="M6.6 10.8c1.4 2.8 3.8 5.1 6.6 6.6l2.2-2.2c.3-.3.7-.4 1-.2 1.1.4 2.3.6 3.6.6.6 0 1 .4 1 1V20c0 .6-.4 1-1 1C10.6 21 3 13.4 3 4c0-.6.4-1 1-1h3.5c.6 0 1 .4 1 1 0 1.3.2 2.5.6 3.6.1.3 0 .7-.2 1z" fill="var(--orange)"/></svg>
  <span>052 718 940</span>
</div>
<div class="contact-row" style="top:1094px;font-size:5.5px">
  <svg width="6" height="5" viewBox="0 0 12 10"><rect x="0" y="1" width="12" height="8" rx="1" fill="var(--orange)"/><path d="M0 2l6 4 6-4" fill="none" stroke="#fff"/></svg>
  <span>info@nestivo.com</span>
</div>
<div class="contact-row" style="top:1108px;font-size:5.5px;line-height:9.3px">
  <svg width="5" height="7" viewBox="0 0 10 14"><path d="M5 0a5 5 0 0 1 5 5c0 4-5 9-5 9S0 9 0 5a5 5 0 0 1 5-5z" fill="var(--orange)"/><circle cx="5" cy="5" r="2" fill="#fff"/></svg>
  <span><span style="color:var(--orange)">NESTIVO</span><br>PO 612, Larkfield, Victoria 3299,<br>AUSTRALIA</span>
</div>

<h4 class="footer-heading" style="left:370px">Quick Links</h4>
<ul class="quick-links">
  <li>Privacy</li><li>Terms &amp; Conditions</li><li>Investment</li><li>Media</li><li>NGO/Government</li><li>Contact</li><li>Sitemap</li>
</ul>

<h4 class="footer-heading" style="left:454px">Subscribe Newsletter</h4>
<div class="newsletter-input">name@email.com</div>
<div class="btn btn-orange" style="left:454px;top:1108px;width:52px;height:18px">Subscribe</div>

<div class="copyright">2023 <b>Nestivo</b>. All Rights Reserved.</div>
<svg class="abs" style="left:662px;top:1159px" width="15" height="18" viewBox="0 0 15 18"><path d="M7.5 0L15 18 7.5 13 0 18z" fill="var(--blue)"/></svg>

</body>
</html>
```